KeyNestly - Apartment Reviews Website Concept Sketch

IMPORTANT UPDATES BELOW -

Current Contest:
Deliverable: 1 or more original design concepts for website home-page. A guaranteed payment will be made to the lead design.

Context:
This guaranteed-payment contest is for submission of 1 or more concept sketches for the home page of the website described below.

Based on finalist submissions, a freelance contract may be let for design-only development (PSDs only) of the full site, approximately 20 pages. Budget for the full site design is $3000 - $5000 and will include multiple rounds to refine the home-page concept and then to extend the design to the full site.

All mySql and PHP logic is already coded and working. No coding is required for the contest or the follow-on project.

IMPORTANT UPDATES ABOVE -

The Website:

KeyNestly is developing an on-line, searchable, pay-for-access database of user-contributed reviews of apartment complexes. Consumers will use these reviews to make better informed decisions before committing to an apartment lease.

We currently have a functional, wireframe-only website accessible at keynestly.example. The wireframes are under development, and site pages may display debugging information or may be inaccessible on occasion.

Additional information as well as a site map is available at: keynestly.example/pbstudio.

We require complete graphic design for a multi-page, interactive, database-driven website. Cutting and coding the design into the existing php code base is a separate project, but feel free to quote on this separately if you have capabilities. We do not require any software or database development. All software is proprietary, we are not using any third-party platform for CMS, survey management, etc.

Attributes we wish to convey with our logo, website, and other presentation:
• Trustworthiness – users should expect the information we present to be accurate and complete
• Impartiality - users can rely on the survey results we present not to be influenced or “bought” by apartment managers
• Professionalism – KeyNestly is a team of professionals dedicated to building and delivering a high-value, high-relevance database of fresh information that will help apartment renters make better decisions about where to live. We are not an informal community, not a group of volunteers, and not a free-access, open source product.
• Simplicity – our site is easy to use, easy to search, and our survey results are easy to understand
• Accessibility – anyone can use our service, it is not just for experts or people with technical skills
• Affordability – our service is priced at a point (about $50 for 90-days use) that it is affordable for everyone who plans to rent an apartment and makes economic sense as insurance against making an uninformed decision (much less than the cost of a month’s rent)
• Interest to Apartment Dwellers – our name, and preferably our logo, identifies us immediately as being of interest to apartment renters and seekers
• Positive Outlook – although the greatest value of KeyNestly will be in helping apartment hunters avoid buildings with construction, management, and neighborhood problems, our website imagery should not focus on the negative aspects, but rather on the happiness, security, and satisfaction that comes with a good selection of an apartment

Website Purpose
During Phase 1 (current) of KeyNestly’s development, the purpose of the website is to collect apartment reviews. Traffic will be driven by a display/performance ad campaign. We are assembling a business asset (the database) and this is really a direct response marketing campaign. We will offer a variety of incentives (sweepstakes entries, gift card redemption) to induce people to complete a survey and view a series of advertising offers. During Phase 1, there will be no database of apartment reviews for users to preview, and nothing for us to sell.

During Phase 2 (future) of KeyNestly’s development, the purpose of the website will be to induce members to pay to access the database, and to provide a means for paying customers to access the database of reviews. Phase 2 is NOT in scope at this time, but will represent a substantial future upgrade - naturally the original design team will be in a strong competitive position for this future work.

The KeyNestly website has a small area that will serve our advertising partners so they can access campaign and reporting information. This part of the site will need a simple but professional design treatment and is within the scope of Phase 1 development.

Our primary creative goal at this time is to present a website that supports Phase 1 goals. Many of the pages necessary for Phase 2 operation are outside the scope of the Phase 1 creative effort, in particular previewing reviews, searching the database, viewing search results, and transaction-oriented pages.
Updates

Project Deadline Extended
Reason: We didn't communicate the nature of the Design Contest well. We are extending the deadline to permit designers to re-evaluate the scope of the current work in the context of the award amount.

Target Market(s)

Our market audience is internet-savvy Americans who live in or are moving into an apartment.

Industry/Entity Type

Graphic Design

Requirements
Must have
• We are finalizing logo design and have posted a draft copy on the site. Logo design is still subject to refinement, but the basic concept is frozen. Colors / combinations may change, but will be arena of blue or blue+green.

Key elements of the home page are:
- a call to action to review an apartment
- room for 1-2 rotating articles about selecting an apartment, planning a move, shopping for insurance in your new location, etc. to act as light-weight, added value elements for site visitors.

Important to know:
- The survey itself (reviewapartment.php - only accessible by following all the steps starting with the "review an apartment" link) is database-driven, so the design must be able to accommodate assembly of questions in different formats using a building-block approach. The current wire-frame illustrates the major question/answer formats: radio; checkbox; matrix-radio; free-text.

Over the life of the project, we will undoubtedly build dozens of landing pages that center around the call to action of "review the apartment where you live" with various inducements (sweepstakes entry, redeemable incentives, social appeals, etc.) Development of these landing pages is a separate project, but the initial design should include one or two. If direct-marketing design / landing page design is not your forte, these pages can be removed from the scope of the web design project.

Should not have
• We would prefer to stay away from flash-heavy pages for the website.

```html
<!DOCTYPE html>
<html lang="en">
<head>
<meta charset="utf-8">
<title>KeyNestly – Home</title>
<link href="https://fonts.googleapis.com/css2?family=Ubuntu:wght@300;400;500;700&family=PT+Sans:ital,wght@0,400;0,700;1,400&display=swap" rel="stylesheet">
<style>
:root{
  --bg-green:#66cc44;
  --brand-green:#7ab800;
  --title-green:#6aa61a;
  --btn-green-top:#4cc21e;
  --btn-green-bot:#1f9a0a;
  --nav-blue-top:#2f77b8;
  --nav-blue-bot:#0d4a8c;
  --deep-blue:#0b4c9a;
  --link-blue:#1f6fc2;
  --sky-blue:#1e90ff;
  --orange:#ff7a12;
  --panel-grey:#5a5a5a;
  --label-yellow:#e4ef8a;
  --text-dark:#333333;
  --text-grey:#777777;
  --row-a:#eeeeee;
  --row-b:#e2e2e2;
  --white:#ffffff;
}
*{box-sizing:border-box;margin:0;padding:0}
html,body{width:1193px;height:1200px;overflow:hidden;background:var(--bg-green)}
body{font-family:"Ubuntu",sans-serif;color:var(--text-dark)}
.stage{position:absolute;left:0;top:0;width:1134px;height:1141px;transform:scale(1.052,1.0517);transform-origin:0 0}
.abs{position:absolute}
.sheet{position:absolute;left:51px;top:26px;width:1024px;height:1064px;background:var(--white);border-radius:8px;box-shadow:0 1px 4px rgba(0,0,0,.25);overflow:hidden}

/* header */
.brand{left:78px;top:78px;display:flex;align-items:center;gap:8px}
.brand-mark{width:16px;height:16px;background:var(--brand-green)}
.brand-name{font-family:"Ubuntu",sans-serif;font-weight:700;font-size:32px;color:var(--brand-green);letter-spacing:-.5px}
.tagline{left:308px;top:90px;font-family:"PT Sans",sans-serif;font-style:italic;font-size:20px;color:#8a8a8a}
.util-links{left:613px;top:47px;font-size:12px;color:#5aa7d8;font-weight:300}
.util-links span{margin:0 6px;color:#8bbfe0}
.survey-btn{left:889px;top:41px;width:172px;height:30px;border-radius:3px;background:linear-gradient(#2fa3ff,#0a7fe6);color:#fff;font-weight:500;font-size:16px;display:flex;align-items:center;justify-content:center}
.create{left:883px;top:108px;font-size:12px;font-weight:500;color:#333}
.login{left:1008px;top:101px;width:52px;height:26px;background:linear-gradient(#ff9a3a,var(--orange));color:#fff;font-size:12px;font-weight:500;display:flex;align-items:center;justify-content:center;border-radius:2px}

/* nav */
.nav{left:51px;top:141px;width:1024px;height:38px;background:linear-gradient(var(--nav-blue-top),var(--nav-blue-bot));display:flex}
.nav a{color:#fff;text-decoration:none;font-size:16px;font-weight:500;display:flex;align-items:center;padding:0 17px}
.nav .active{background:linear-gradient(#4caf2a,#2c8a12);padding:0 18px}
.nav .account{margin-left:auto;background:linear-gradient(#5a8fc4,#3f77ad);width:128px;justify-content:center}

/* hero */
.hero{left:51px;top:179px;width:636px;height:303px;background:linear-gradient(180deg,#5f9ed8 0%,#a9cbe6 40%,#d8dcd8 62%,#5d6a4c 100%)}
.hero-bar{left:51px;top:414px;width:636px;height:68px;background:rgba(30,30,30,.82)}
.hero-title{left:62px;top:425px;color:#fff;font-size:17px;font-weight:400}
.hero-reviews{left:65px;top:454px;font-size:11px;color:#56b7ff}
.read-more{left:140px;top:451px;width:76px;height:20px;background:#69b9f5;color:#0d2d55;font-size:11px;font-weight:700;display:flex;align-items:center;justify-content:center}
.thumb{top:426px;width:45px;height:44px;background:linear-gradient(#6ea7da,#d7dad6 60%,#6a7759);border:1px solid #ccc}
.thumb.current{border:2px solid #8fc8ff}

/* search */
.search-title{left:698px;top:190px;font-size:26px;color:var(--title-green);font-weight:400}
.search-title b{color:var(--deep-blue);font-weight:500}
.search-panel{left:694px;top:229px;width:374px;height:226px;background:var(--panel-grey);border-radius:4px}
.field-label{font-size:15px;font-weight:700;color:var(--label-yellow);text-align:right}
.input{background:#fff;border-radius:2px;height:34px;font-size:13px;display:flex;align-items:center;padding-left:8px;font-family:"PT Sans",sans-serif}
.input.placeholder{color:#9a9a9a}
.select::after{content:"";position:absolute;right:8px;top:14px;border-left:6px solid transparent;border-right:6px solid transparent;border-top:7px solid #666}
.to{left:936px;top:368px;font-size:10px;color:#ccc;font-weight:700}
.search-btn{left:935px;top:411px;width:123px;height:38px;background:linear-gradient(var(--btn-green-top),#2aa814);color:#fff;font-weight:700;font-size:15px;display:flex;align-items:center;justify-content:center;border-radius:2px}

/* featured */
.featured-bar{left:51px;top:482px;width:636px;height:48px;background:linear-gradient(#9fd64a,#6cbd2a)}
.featured-title{left:64px;top:488px;font-size:28px;font-weight:300;color:#1a1a1a}
.view-more-top{left:591px;top:489px;width:90px;height:35px;background:linear-gradient(#3da018,#237a08);border-radius:3px;color:#c8f0a4;font-size:16px;display:flex;align-items:center;justify-content:center}
.card{width:137px}
.card-photo{width:137px;height:136px}
.card-title{margin-top:6px;font-size:13px;line-height:16px;color:var(--title-green);font-weight:500;height:40px}
.card-reviews{margin-top:4px;font-size:12px;color:var(--link-blue);text-decoration:underline;font-weight:500}
.card-btn{margin-top:15px;width:133px;height:28px;background:linear-gradient(var(--btn-green-top),var(--btn-green-bot));border-radius:2px;color:#fff;font-size:13px;font-weight:500;display:flex;align-items:center;justify-content:center}
.photo-a{background:linear-gradient(#9ec6ea,#dfe4e6 45%,#4d7d32)}
.photo-b{background:linear-gradient(#3d8fd0,#e8dcc6 50%,#3fb4e0)}
.photo-c{background:linear-gradient(#6fa6d8,#c9a56a 45%,#5a4a3c)}
.photo-d{background:linear-gradient(#cfe2ee,#a28a6c 50%,#d8d2c4)}

/* ad */
.ad-frame{left:694px;top:489px;width:375px;height:152px;border:1px solid #444}
.ad-art{left:701px;top:496px;width:361px;height:138px;background:linear-gradient(90deg,#ff9a00,#ffb300)}
.ad-panel{left:838px;top:507px;width:224px;height:92px;background:#3b2a08;border-radius:10px 0 0 10px}
.ad-apply{left:856px;top:506px;color:#fff;font-size:48px;font-weight:700}
.ad-sub{left:856px;top:563px;color:#fff;font-size:11px;font-weight:500}
.ad-bank{left:978px;top:604px;width:80px;height:26px;background:#fff;color:var(--deep-blue);font-size:10px;font-weight:500;display:flex;align-items:center;justify-content:center}

/* top rated */
.top-head{left:694px;top:650px;width:374px;height:52px;background:linear-gradient(#3a86cc,#0d4a92)}
.top-title{left:701px;top:658px;color:#fff;font-size:29px;font-weight:300}
.top-list{left:694px;top:703px;width:374px;list-style:none}
.top-list li{height:37px;display:flex;align-items:center;justify-content:space-between;padding:0 10px 0 12px;font-size:13px;font-family:"PT Sans",sans-serif;color:#333;background:var(--row-a);border-bottom:1px solid #fff}
.top-list li:nth-child(even){background:var(--row-b)}
.top-list a{font-size:11px;color:var(--link-blue);text-decoration:underline}

/* footer */
.footer{top:1104px;font-size:12px;color:#2a5a14}
.footer span{margin:0 8px}
</style>
</head>
<body>
<div class="stage">
  <div class="sheet"></div>

  <header>
    <div class="abs brand"><span class="brand-mark"></span><span class="brand-name">KeyNestly</span></div>
    <div class="abs tagline">“Before you rent, hear what the neighbors say”</div>
    <div class="abs util-links">Privacy policy<span>|</span>Terms &amp; Conditions<span>|</span>FAQ</div>
    <div class="abs survey-btn">Take Your Survey</div>
    <div class="abs create">CREATE AN ACCOUNT</div>
    <div class="abs login">LOGIN</div>
  </header>

  <nav class="abs nav">
    <a class="active">Home</a><a>About Us</a><a>Look Up Apartments</a><a>Enter Sweeps</a><a>Contest Rurle</a><a class="account">My Account</a>
  </nav>

  <section>
    <div class="abs hero" role="img" aria-label="Photo of a white two-storey house with porch under a blue sky"></div>
    <div class="abs hero-bar"></div>
    <div class="abs hero-title">RIO GRANDE VALLEY HOUSING ESTATE</div>
    <div class="abs hero-reviews">21 Reviews</div>
    <div class="abs read-more">READ MORE</div>
    <div class="abs thumb current" style="left:469px" role="img" aria-label="Thumbnail of house photo"></div>
    <div class="abs thumb" style="left:524px" role="img" aria-label="Thumbnail of house photo"></div>
    <div class="abs thumb" style="left:578px" role="img" aria-label="Thumbnail of house photo"></div>
    <div class="abs thumb" style="left:632px" role="img" aria-label="Thumbnail of house photo"></div>
  </section>

  <section>
    <h2 class="abs search-title">Find Perfect Home for <b>RENT</b></h2>
    <div class="abs search-panel"></div>
    <div class="abs field-label" style="left:700px;top:244px">FAND A HOME IN</div>
    <div class="abs input placeholder" style="left:827px;top:237px;width:233px">Place or Postcode</div>
    <div class="abs field-label" style="left:743px;top:285px">BEDROOM</div>
    <div class="abs input select" style="left:827px;top:277px;width:103px">3</div>
    <div class="abs field-label" style="left:732px;top:327px">BATHROOM</div>
    <div class="abs input select" style="left:827px;top:317px;width:103px">2</div>
    <div class="abs field-label" style="left:756px;top:366px">BUDGET</div>
    <div class="abs input select" style="left:827px;top:357px;width:103px">$400</div>
    <div class="abs to">TO</div>
    <div class="abs input select" style="left:957px;top:357px;width:103px">$600</div>
    <div class="abs search-btn">SEARCH</div>
  </section>

  <section>
    <div class="abs featured-bar"></div>
    <h2 class="abs featured-title">Featured Homes</h2>
    <div class="abs view-more-top">View More</div>

    <div class="abs card" style="left:69px;top:547px"><div class="card-photo photo-a" role="img" aria-label="Photo of a two-storey family house"></div><div class="card-title">3BHK Nort Facing Appartment</div><div class="card-reviews">8 Reviews</div><div class="card-btn">View More</div></div>
    <div class="abs card" style="left:224px;top:547px"><div class="card-photo photo-b" role="img" aria-label="Photo of apartment with swimming pool"></div><div class="card-title">4BHK apartment with Swimming pool</div><div class="card-reviews">6 Reviews</div><div class="card-btn">View More</div></div>
    <div class="abs card" style="left:380px;top:547px"><div class="card-photo photo-c" role="img" aria-label="Photo of house with garage"></div><div class="card-title">3BHK House In Ground Floor with Garrage</div><div class="card-reviews">6 Reviews</div><div class="card-btn">View More</div></div>
    <div class="abs card" style="left:535px;top:547px"><div class="card-photo photo-d" role="img" aria-label="Photo of stone villa with fountain"></div><div class="card-title">3BHK Nort Facing Appartment</div><div class="card-reviews">4 Reviews</div><div class="card-btn">View More</div></div>

    <div class="abs card" style="left:69px;top:824px"><div class="card-photo photo-a" role="img" aria-label="Photo of a two-storey family house"></div><div class="card-title">3BHK Nort Facing Appartment</div><div class="card-reviews">8 Reviews</div><div class="card-btn">View More</div></div>
    <div class="abs card" style="left:224px;top:824px"><div class="card-photo photo-b" role="img" aria-label="Photo of apartment with swimming pool"></div><div class="card-title">4BHK apartment with Swimming pool</div><div class="card-reviews">6 Reviews</div><div class="card-btn">View More</div></div>
    <div class="abs card" style="left:380px;top:824px"><div class="card-photo photo-c" role="img" aria-label="Photo of house with garage"></div><div class="card-title">3BHK House In Ground Floor with Garrage</div><div class="card-reviews">6 Reviews</div><div class="card-btn">View More</div></div>
    <div class="abs card" style="left:535px;top:824px"><div class="card-photo photo-d" role="img" aria-label="Photo of stone villa with fountain"></div><div class="card-title">3BHK Nort Facing Appartment</div><div class="card-reviews">4 Reviews</div><div class="card-btn">View More</div></div>
  </section>

  <aside>
    <div class="abs ad-frame"></div>
    <div class="abs ad-art" role="img" aria-label="Illustration of hands holding a small house on orange background"></div>
    <div class="abs ad-panel"></div>
    <div class="abs ad-apply">Apply</div>
    <div class="abs ad-sub">For your Home Loan in 5 min.</div>
    <div class="abs ad-bank">Harborline Bank</div>

    <div class="abs top-head"></div>
    <h2 class="abs top-title">10 Top Rated Homes</h2>
    <ul class="abs top-list">
      <li>3BHK North Facing Appartment<a>34 Reviews</a></li>
      <li>Long Living Room, 2 BHK Appartment<a>30 Reviews</a></li>
      <li>2 bedroom with Car Parking, Pool<a>30 Reviews</a></li>
      <li>3BHK North Facing Appartment<a>28 Reviews</a></li>
      <li>Long Living Room, 2 BHK Appartment<a>27 Reviews</a></li>
      <li>2 bedroom with Car Parking, Pool<a>21 Reviews</a></li>
      <li>3BHK North Facing Appartment<a>20 Reviews</a></li>
      <li>Long Living Room, 2 BHK Appartment<a>19 Reviews</a></li>
      <li>2 bedroom with Car Parking, Pool<a>19 Reviews</a></li>
      <li>3BHK North Facing Appartment<a>17 Reviews</a></li>
    </ul>
  </aside>

  <footer>
    <div class="abs footer" style="left:59px">copyright 2012. KeyNestly LLC.</div>
    <div class="abs footer" style="left:326px">Privacy policy<span>|</span>Terms &amp; Conditions<span>|</span>FAQ</div>
  </footer>
</div>
</body>
</html>
```